Mental Health care Company in Washington DC

We are a new mental health care services provider in Washington DC. Please look at these sites.
https://marlowbrookpartners.com
https://www.quillstoneinc.com
https://velmarsh-kt.org/
https://www.trivanqx.com
https://www.thelanternofqz.com

```html
<!DOCTYPE html>
<html lang="en">
<head>
<meta charset="utf-8">
<title>Velora Health Services – Mental Health Care in Washington</title>
<link href="https://fonts.googleapis.com/css2?family=Poppins:wght@400;500;600;700&display=swap" rel="stylesheet">
<style>
:root{
  --orange:#F58220;
  --teal:#A3D9DC;
  --teal-soft:#E4F5F6;
  --navy:#0E1E45;
  --peach:#FDE8D8;
  --cream:#FBF7F0;
  --card:#F1F9FA;
  --text:#3C4558;
  --white:#FFFFFF;
}
*{box-sizing:border-box;margin:0;padding:0}
html,body{width:1200px;height:3413px;overflow:hidden}
body{font-family:'Poppins',sans-serif;color:var(--navy);background:var(--white);position:relative}
.abs{position:absolute}
.btn{position:absolute;display:flex;align-items:center;justify-content:space-between;gap:14px;height:42px;padding:0 18px 0 20px;border-radius:21px;font-size:12px;font-weight:600;color:var(--white);background:var(--orange);white-space:nowrap}
.btn.teal{background:var(--teal)}
.btn.outline{background:var(--white);color:var(--navy);border:1.5px solid var(--navy)}
.btn.white{background:var(--white);color:var(--navy)}
.btn svg{width:14px;height:14px}
.photo{position:absolute}
/* header */
.site-header{position:absolute;left:0;top:0;width:1200px;height:73px;background:var(--white)}
.brand{position:absolute;left:122px;top:12px;width:172px;color:var(--navy)}
.brand-name{display:block;font-size:26px;font-weight:600;line-height:30px;letter-spacing:-.5px;white-space:nowrap}
.brand-tag{display:block;font-size:10px;font-weight:400;letter-spacing:6px;line-height:14px;text-align:center;color:var(--navy)}
.brand-dot{display:inline-block;width:10px;height:10px;border-radius:50%;background:var(--orange);margin-right:6px;vertical-align:middle}
.nav{position:absolute;left:320px;top:30px;display:flex;gap:23px;font-size:13px;color:var(--navy)}
.icon-btn{position:absolute;top:26px;width:22px;height:22px;border:1.5px solid var(--navy);border-radius:50%}
/* hero */
.hero{position:absolute;left:0;top:73px;width:1200px;height:600px}
.hero-kicker{position:absolute;left:119px;top:230px;font-size:14px;color:var(--white)}
.hero-title{position:absolute;left:118px;top:250px;font-size:47px;line-height:57px;font-weight:600;color:var(--white)}
.hero-sub{position:absolute;left:120px;top:365px;font-size:20px;font-weight:500;color:var(--white)}
.section-title{position:absolute;width:1200px;text-align:center;font-size:32px;font-weight:500;color:var(--navy)}
.svc-card{position:absolute;width:228px;height:237px;background:var(--card)}
.svc-card .photo{left:6px;top:6px;width:216px;height:172px}
.svc-card .label{position:absolute;left:64px;top:190px;font-size:15px;font-weight:500;line-height:18px;color:var(--navy)}
.svc-card .ic{position:absolute;left:14px;top:192px;width:34px;height:28px}
.arrow-circ{position:absolute;width:20px;height:20px;border:1.5px solid var(--navy);border-radius:50%}
.band{position:absolute;left:0;width:1200px;background:#FCEFE8}
/* about */
.about-box{position:absolute;left:653px;top:1250px;width:428px;height:366px;background:var(--peach)}
.kicker{font-size:13px;color:var(--orange)}
.body-text{font-size:11.5px;line-height:18px;color:var(--text)}
/* why */
.why{position:absolute;left:0;top:1673px;width:1200px;height:433px;background:var(--teal)}
.why h2{position:absolute;left:122px;top:42px;font-size:32px;line-height:38px;font-weight:600;color:var(--white)}
.feat{position:absolute;width:220px;color:var(--white)}
.feat h3{font-size:17px;font-weight:500;line-height:20px;padding-left:24px;position:relative}
.feat h3 svg{position:absolute;left:0;top:3px;width:16px;height:16px}
.feat p{font-size:11px;line-height:16px;padding-left:24px;margin-top:4px}
/* focus */
.focus{position:absolute;top:2106px;width:600px;height:320px}
.focus .photo{left:122px;top:50px;width:168px;height:240px;border-radius:84px/120px;border:5px solid var(--white)}
.focus h3{position:absolute;font-size:19px;font-weight:500}
.t-card{position:absolute;width:228px;height:228px;background:var(--card)}
.t-card .photo{left:5px;top:5px;width:218px;height:172px}
.t-card .label{position:absolute;left:0;top:194px;width:228px;text-align:center;font-size:15px;font-weight:500}
/* cta + footer */
.footer{position:absolute;left:0;top:3031px;width:1200px;height:382px;background:var(--navy)}
.cta{position:absolute;left:197px;top:2897px;width:806px;height:222px;background:var(--orange);text-align:center}
.cta h2{margin-top:44px;font-size:32px;font-weight:600;color:var(--white)}
.cta p{margin-top:8px;font-size:12px;line-height:15px;color:var(--white)}
.fcol{position:absolute;top:3152px;color:var(--white)}
.fcol h4{font-size:15px;font-weight:500;margin-bottom:20px}
.fcol ul{list-style:none;font-size:10px;line-height:22px}
.fitem{position:relative;padding-left:32px;font-size:9.5px;line-height:12px;margin-bottom:16px}
.fitem .circ{position:absolute;left:0;top:0;width:22px;height:22px;border:1.5px solid var(--white);border-radius:50%}
.vline{position:absolute;top:3150px;width:1px;height:212px;background:rgba(255,255,255,.25)}
</style>
</head>
<body>

<header class="site-header">
  <div class="brand"><span class="brand-name">Velora Health</span><span class="brand-tag">SERVICES</span></div>
  <nav class="nav"><span>About us</span><span>Therapies &amp; Treatment</span><span>Services</span><span>Gallery</span><span>Contact us</span></nav>
  <div class="btn" style="left:810px;top:20px;height:34px;font-size:11px;gap:10px;padding:0 13px 0 15px">Schedule an Appointment <svg viewBox="0 0 14 14"><path d="M2 7h10M8 3l4 4-4 4" stroke="#fff" stroke-width="1.6" fill="none"/></svg></div>
  <div class="icon-btn" style="left:1026px"></div>
  <div class="icon-btn" style="left:1056px"><svg viewBox="0 0 22 22" width="19" height="19"><circle cx="9.5" cy="9.5" r="4" stroke="#0E1E45" stroke-width="1.5" fill="none"/><path d="M12.5 12.5l3 3" stroke="#0E1E45" stroke-width="1.5"/></svg></div>
</header>

<section class="hero">
  <div class="photo" role="img" aria-label="Woman meditating cross-legged in a grassy field under a cloudy sky" style="left:0;top:0;width:1200px;height:600px;background:linear-gradient(180deg,#8E969B 0%,#6F7A6E 40%,#4B5A37 75%,#3E4A2E 100%)"></div>
  <div class="hero-kicker">Welcome to Velora Health Services ———————</div>
  <h1 class="hero-title">Empowering Minds<br>Healing Lives –</h1>
  <div class="hero-sub">Mental Health Care in Washington</div>
  <div class="btn" style="left:121px;top:415px">Find a Therapist <svg viewBox="0 0 14 14"><path d="M2 7h10M8 3l4 4-4 4" stroke="#fff" stroke-width="1.6" fill="none"/></svg></div>
  <div class="btn teal" style="left:287px;top:415px">Request a Demo <svg viewBox="0 0 14 14"><path d="M2 7h10M8 3l4 4-4 4" stroke="#fff" stroke-width="1.6" fill="none"/></svg></div>
</section>

<h2 class="section-title" style="top:712px">Services We Offer</h2>
<div class="arrow-circ" style="left:81px;top:876px"><svg viewBox="0 0 20 20"><path d="M11 6l-4 4 4 4" stroke="#0E1E45" stroke-width="1.5" fill="none"/></svg></div>
<div class="arrow-circ" style="left:1100px;top:876px"><svg viewBox="0 0 20 20"><path d="M8 6l4 4-4 4" stroke="#0E1E45" stroke-width="1.5" fill="none"/></svg></div>

<div class="svc-card" style="left:121px;top:779px">
  <div class="photo" role="img" aria-label="Therapist and client in an individual session" style="background:linear-gradient(160deg,#E8E2DA,#A9A39A)"></div>
  <svg class="ic" viewBox="0 0 34 28"><path d="M17 26C10 20 10 10 17 4c7 6 7 16 0 22z" fill="#A3D9DC"/><path d="M17 26C9 26 3 20 2 12c8 1 14 6 15 14zM17 26c8 0 14-6 15-14-8 1-14 6-15 14z" fill="#F58220"/></svg>
  <div class="label">Individual<br>Therapy</div>
</div>
<div class="svc-card" style="left:365px;top:779px">
  <div class="photo" role="img" aria-label="Counsellor with a couple on a sofa" style="background:linear-gradient(160deg,#E7E4DE,#9B8F86)"></div>
  <svg class="ic" viewBox="0 0 34 28"><circle cx="9" cy="6" r="5" fill="#F58220"/><circle cx="25" cy="6" r="5" fill="#A3D9DC"/><rect x="2" y="13" width="14" height="14" rx="6" fill="#A3D9DC"/><rect x="18" y="13" width="14" height="14" rx="6" fill="#F58220"/></svg>
  <div class="label">Couples and<br>Family Counseling</div>
</div>
<div class="svc-card" style="left:609px;top:779px">
  <div class="photo" role="img" aria-label="Counsellor talking with a man at a table" style="background:linear-gradient(160deg,#EFE9E2,#8C8075)"></div>
  <svg class="ic" viewBox="0 0 34 28"><circle cx="17" cy="7" r="6" fill="#F58220"/><rect x="2" y="16" width="30" height="10" rx="5" fill="#A3D9DC"/></svg>
  <div class="label">Substance Abuse<br>Addiction Counseling</div>
</div>
<div class="svc-card" style="left:853px;top:779px">
  <div class="photo" role="img" aria-label="Child playing alone on a wooden floor" style="background:linear-gradient(160deg,#D9DCDF,#6F6A66)"></div>
  <svg class="ic" viewBox="0 0 34 28"><circle cx="17" cy="9" r="8" fill="#F58220"/><path d="M3 27c2-8 26-8 28 0z" fill="#A3D9DC"/></svg>
  <div class="label">Child and<br>Adolescent Issues</div>
</div>
<div class="btn" style="left:521px;top:1042px;height:41px">View All Services <svg viewBox="0 0 14 14"><path d="M2 7h10M8 3l4 4-4 4" stroke="#fff" stroke-width="1.6" fill="none"/></svg></div>

<div class="band" style="top:1122px;height:66px"></div>

<section class="abs" style="left:0;top:1188px;width:1200px;height:485px;background:var(--cream)">
  <div class="photo" role="img" aria-label="Young caregiver embracing a smiling older woman on a sofa" style="left:0;top:0;width:720px;height:485px;background:linear-gradient(120deg,#A8ACA3,#D5CBBE 55%,#EFE9DE)"></div>
</section>
<div class="about-box">
  <div class="kicker" style="position:absolute;left:44px;top:38px">About Us ——————</div>
  <h2 style="position:absolute;left:43px;top:54px;font-size:31px;line-height:37px;font-weight:500">Welcome to<br>Velora Health Services</h2>
  <p class="body-text" style="position:absolute;left:44px;top:136px;width:345px">At Velora Health Services, we are committed to providing top notch health consulting services to our clients. Our mission is to help people achieve optimal health and wellness through personalized plans and ongoing support. Our team of experienced health consultants has a diverse range of expertise, from nutrition and fitness to stress management and holistic health.</p>
  <div class="btn" style="left:44px;top:283px">Read More <svg viewBox="0 0 14 14"><path d="M2 7h10M8 3l4 4-4 4" stroke="#fff" stroke-width="1.6" fill="none"/></svg></div>
  <div class="btn outline" style="left:182px;top:283px">Meet Our Team <svg viewBox="0 0 14 14"><path d="M2 7h10M8 3l4 4-4 4" stroke="#0E1E45" stroke-width="1.6" fill="none"/></svg></div>
</div>

<section class="why">
  <h2>Why Choose Us<br>Velora Health Services?</h2>
  <div class="feat" style="left:122px;top:152px"><h3><svg viewBox="0 0 16 16"><circle cx="8" cy="8" r="8" fill="#fff"/><path d="M4.5 8l2.3 2.3L11.5 5.7" stroke="#A3D9DC" stroke-width="1.8" fill="none"/></svg>Assessment</h3><p>In just 3-5 minutes, you'll answer some questions that can help identify areas where you might need support.</p></div>
  <div class="feat" style="left:386px;top:152px"><h3><svg viewBox="0 0 16 16"><circle cx="8" cy="8" r="8" fill="#fff"/><path d="M4.5 8l2.3 2.3L11.5 5.7" stroke="#A3D9DC" stroke-width="1.8" fill="none"/></svg>Dedicated Guidance</h3><p>Meet with your Care Navigator for clinical guidance and emotional support throughout your journey.</p></div>
  <div class="feat" style="left:122px;top:265px"><h3><svg viewBox="0 0 16 16"><circle cx="8" cy="8" r="8" fill="#fff"/><path d="M4.5 8l2.3 2.3L11.5 5.7" stroke="#A3D9DC" stroke-width="1.8" fill="none"/></svg>Personalized<br>Recommendations</h3><p>You'll receive a care plan based on your goals and assessment results, including a curated list of providers from our diverse network.</p></div>
  <div class="feat" style="left:386px;top:265px"><h3><svg viewBox="0 0 16 16"><circle cx="8" cy="8" r="8" fill="#fff"/><path d="M4.5 8l2.3 2.3L11.5 5.7" stroke="#A3D9DC" stroke-width="1.8" fill="none"/></svg>Inclusive Care</h3><p>Quickly browse and schedule appointments with the provider who best fits your needs and preferences – or get started with on-demand digital exercises.</p></div>
</section>

<section class="focus" style="left:0;background:var(--peach)">
  <div class="photo" role="img" aria-label="Therapist listening to a client in a calm office" style="background:linear-gradient(160deg,#8E8276,#4D443D)"></div>
  <h3 style="left:318px;top:80px">Our Treatment Focus</h3>
  <p class="body-text" style="position:absolute;left:318px;top:116px;width:262px">Our focus is to help individuals heal, energize, and become aware of their inner strengths. We achieve this by providing a neutral safe space, listening to your concerns, and customizing a treatment plan.</p>
  <div class="btn" style="left:318px;top:220px">Click Here <svg viewBox="0 0 14 14"><path d="M2 7h10M8 3l4 4-4 4" stroke="#fff" stroke-width="1.6" fill="none"/></svg></div>
</section>
<section class="focus" style="left:600px;background:var(--teal-soft)">
  <div class="photo" role="img" aria-label="Hands held together in comfort" style="left:34px;background:linear-gradient(160deg,#D8C3B2,#46536A)"></div>
  <h3 style="left:230px;top:82px">Our Patient Promise</h3>
  <p class="body-text" style="position:absolute;left:230px;top:118px;width:252px">We promise to be there for you every step of your journey. Our goal is to help you grow from your struggles, heal from your pain, and move forward to where you want to be in your life.</p>
  <div class="btn teal" style="left:230px;top:222px">Click Here <svg viewBox="0 0 14 14"><path d="M2 7h10M8 3l4 4-4 4" stroke="#fff" stroke-width="1.6" fill="none"/></svg></div>
</section>

<h2 class="section-title" style="top:2474px">Our Treatment Approach and Therapy</h2>
<div class="arrow-circ" style="left:85px;top:2637px"><svg viewBox="0 0 20 20"><path d="M11 6l-4 4 4 4" stroke="#0E1E45" stroke-width="1.5" fill="none"/></svg></div>
<div class="arrow-circ" style="left:1091px;top:2637px"><svg viewBox="0 0 20 20"><path d="M8 6l4 4-4 4" stroke="#0E1E45" stroke-width="1.5" fill="none"/></svg></div>
<div class="t-card" style="left:121px;top:2543px"><div class="photo" role="img" aria-label="Distressed woman curled up on the floor" style="background:linear-gradient(160deg,#E3E1DE,#8D8A86)"></div><div class="label">Trauma &amp; PTSD</div></div>
<div class="t-card" style="left:365px;top:2543px"><div class="photo" role="img" aria-label="Pensive man sitting against a dark wall" style="background:linear-gradient(160deg,#6B4A3C,#2F2824)"></div><div class="label">Depression &amp; Anxiety</div></div>
<div class="t-card" style="left:609px;top:2543px"><div class="photo" role="img" aria-label="Two people holding hands" style="background:linear-gradient(160deg,#EEE8E2,#C59770)"></div><div class="label">Relationships</div></div>
<div class="t-card" style="left:853px;top:2543px"><div class="photo" role="img" aria-label="Therapist and client talking in a bright room with plants" style="background:linear-gradient(160deg,#F1F0EC,#7F8A74)"></div><div class="label">Psychodynamic Therapy</div></div>
<div class="btn" style="left:511px;top:2804px;height:41px">View All Treatment <svg viewBox="0 0 14 14"><path d="M2 7h10M8 3l4 4-4 4" stroke="#fff" stroke-width="1.6" fill="none"/></svg></div>

<div class="band" style="top:2967px;height:64px"></div>

<footer class="footer"></footer>
<div class="cta">
  <h2>You Deserve to Feel Better—Let's Talk</h2>
  <p>We offer confidential, compassionate, and personalized care—because your<br>well-being is our priority. Reach out today and take the first step toward healing.</p>
  <div class="btn teal" style="left:253px;top:141px">Call Us Today <svg viewBox="0 0 14 14"><path d="M2 7h10M8 3l4 4-4 4" stroke="#fff" stroke-width="1.6" fill="none"/></svg></div>
  <div class="btn white" style="left:408px;top:141px;width:146px">Get Started <svg viewBox="0 0 14 14"><path d="M2 7h10M8 3l4 4-4 4" stroke="#F58220" stroke-width="1.6" fill="none"/></svg></div>
</div>

<div class="fcol" style="left:122px;width:200px">
  <div style="margin-bottom:22px;width:172px"><span class="brand-name" style="color:#fff">Velora Health</span><span class="brand-tag" style="color:#fff">SERVICES</span></div>
  <p style="font-size:9.5px;line-height:14px">At Velora Health Services, we are committed to providing top-notch health consulting services to our clients Our mission is to help people achieve optimal health and wellness through personalized plans and ongoing support.</p>
  <div style="display:flex;gap:8px;margin-top:22px">
    <span role="img" aria-label="Social profile" style="width:22px;height:22px;border:1.5px solid #fff;border-radius:50%"></span>
    <span role="img" aria-label="Social profile" style="width:22px;height:22px;border:1.5px solid #fff;border-radius:50%"></span>
    <span role="img" aria-label="Social profile" style="width:22px;height:22px;border:1.5px solid #fff;border-radius:50%"></span>
  </div>
</div>
<div class="vline" style="left:330px"></div>
<div class="fcol" style="left:359px"><h4>Quick links</h4><ul><li>Home</li><li>About us</li><li>Therapies &amp; treatment</li><li>services</li><li>Gallery</li><li>Contact us</li></ul></div>
<div class="vline" style="left:498px"></div>
<div class="fcol" style="left:516px;width:200px"><h4>Contact Us</h4>
  <div class="fitem"><span class="circ"></span>4180 Linden Crest Ave NW,<br>Suite 210 Washington, DC 20011</div>
  <div class="fitem" style="padding-top:5px"><span class="circ"></span>202-555-0148</div>
  <div class="fitem" style="padding-top:5px"><span class="circ"></span>202-555-0172</div>
  <div class="fitem" style="padding-top:5px;color:var(--teal)"><span class="circ"></span>info@veloracare.com</div>
</div>
<div class="vline" style="left:712px"></div>
<div class="fcol" style="left:736px;width:150px"><h4>Opening Hours</h4>
  <div class="fitem"><span class="circ"></span>Mon to Fri<br>09:00 AM – 05:00 PM</div>
  <div class="fitem"><span class="circ"></span>Sat<br>10:00 AM – 02:00 PM</div>
  <div class="fitem" style="margin-top:-8px">Sun Closed</div>
</div>
<div class="vline" style="left:893px"></div>
<div class="fcol" style="left:911px;width:170px"><h4>Subscribe Newsletter</h4>
  <div style="height:36px;border:1.5px solid #fff;border-radius:18px;font-size:10px;line-height:33px;padding-left:16px">Enter Your Email</div>
  <div class="btn" style="position:relative;margin-top:18px;width:158px">Subscribe <svg viewBox="0 0 14 14"><path d="M2 7h10M8 3l4 4-4 4" stroke="#fff" stroke-width="1.6" fill="none"/></svg></div>
</div>
<div class="abs" style="left:122px;top:3370px;width:958px;height:1px;background:rgba(255,255,255,.25)"></div>
<div class="abs" style="left:115px;top:3383px;font-size:9.5px;color:var(--white)">Copyright © 2025 Velora Health Services - All Rights Reserved.</div>
<div class="abs" style="left:802px;top:3383px;font-size:9.5px;color:var(--white);word-spacing:2px">Terms and Conditions &nbsp; | &nbsp; Privacy Policy &nbsp; | &nbsp; Sitemap</div>

</body>
</html>
```